Calendar Ad / Flyer

Our law firm needs a calendar ad to place in a local calendar.
THE DEADLINE IS THIS THURSDAY 06/28/2018.

Attached is the ad used in last years calendar. A few notes on this...
**. This is by no means the model to follow.
Please be creative and do what makes more sense marketing wise.
1. Need to update the color scheme which corresponds to the new website at marvolinlegal.com
2. The "MARVOLIN LAW | SHAPING FAITH WITH RESULTS" should be put at the top and made larger
3. "KNOWN AND TRUSTED IN OUR COMMUNITY FOR OVER 21 YEARS" should be changed to "KNOWN AND TRUSTED IN OUR COMMUNITY FOR OVER 22 YEARS"
4. "Gordon R. Marvolin, Esq." should be made larger and better positioned.
5. Under the list of practices, it should be changed to have:
"Personal Injury, Legal Malpractice, Unlicensed Contractors, Medical Malpractice, Civil Litigation"
6. Contact information (i.e. contact number, website, and address) should be better positioned
7. Placement of endorsement logos should stand out more.
8. New picture of head attorney is attached.

Last but not least... Give it your best shot!

```html
<!DOCTYPE html>
<html lang="en">
<head>
<meta charset="utf-8">
<title>Marvolin Law 2018 Calendar Ad</title>
<link rel="stylesheet" href="https://fonts.googleapis.com/css2?family=Montserrat:wght@400;500;600;700&display=swap">
<style>
:root{
  --ink:#1b1b1b;
  --night:#222;
  --gold:#c9a877;
  --paper:#fff;
  --silver:#d8d8d8;
  --sunday:#e0272e;
  --strip:#cfcfcf;
}
*{margin:0;padding:0;box-sizing:border-box}
html,body{width:1200px;height:877px;overflow:hidden;background:var(--paper)}
body{font-family:"Montserrat",sans-serif;color:var(--ink)}
.ad{position:relative;width:1200px;height:877px;background:var(--night);overflow:hidden}
.skyline{position:absolute;inset:0;background:linear-gradient(180deg,#2a2a2a 0%,#1c1c1c 45%,#262626 70%,#1a1a1a 100%)}

.header{position:absolute;left:0;top:0;width:1200px;height:222px}
.brand{position:absolute;left:42px;top:98px;display:flex;align-items:center;gap:18px}
.brand-mark{width:46px;height:46px;background:var(--gold)}
.brand-name{font-size:54px;font-weight:500;letter-spacing:6px;color:var(--gold);line-height:1}
.tagline{position:absolute;left:106px;top:166px;font-size:21px;font-weight:500;letter-spacing:1.5px;color:var(--silver)}
.attorney-tab{position:absolute;left:575px;top:177px;width:310px;height:45px;background:var(--gold);clip-path:polygon(22px 0,100% 0,100% 100%,0 100%);display:flex;align-items:center;padding-left:30px;font-size:19px;font-weight:600;color:var(--ink);white-space:nowrap}

.practices{position:absolute;left:0;top:222px;width:1200px;height:100px;background:var(--paper)}
.practice-list{width:900px;text-align:center;padding-top:14px;font-size:24px;font-weight:600;line-height:38px;white-space:nowrap}
.practice-list .sep{margin:0 10px}

.contact{position:absolute;left:0;top:322px;width:1200px;height:86px;background:var(--gold);display:flex;align-items:center;padding-left:26px;font-weight:700;white-space:nowrap}
.contact-item{display:flex;align-items:center;gap:8px;font-size:23px;margin-right:18px}
.contact-item svg{flex:none}
.address{font-size:14px;line-height:21px}

.portrait{position:absolute;left:860px;top:12px;width:340px;height:396px;background:linear-gradient(180deg,#bdbdbd 0%,#8c8c8c 55%,#5e5e5e 100%);border-radius:120px 120px 0 0}

.calendar{position:absolute;left:60px;top:436px;width:1080px;display:grid;grid-template-columns:repeat(6,182px);row-gap:52px}
.month h3{text-align:center;font-size:13px;font-weight:600;color:var(--gold);margin-bottom:10px;letter-spacing:.3px;width:130px}
.days{display:grid;grid-template-columns:repeat(7,18px);width:130px;font-size:11px;font-weight:600;color:#f1f1f1;line-height:14.5px;text-align:center;padding-left:4px}
.days span:nth-child(7n+1){color:var(--sunday)}

.year-tab{position:absolute;left:1146px;top:510px;width:54px;height:153px;background:var(--gold)}
.year{position:absolute;left:1103px;top:562px;transform:rotate(-90deg);font-size:46px;font-weight:700;color:var(--gold);background:var(--night);padding:0 6px;line-height:54px;letter-spacing:1px}

.trust{position:absolute;left:30px;top:756px;display:flex;align-items:flex-end;color:var(--gold)}
.trust-lines{text-align:right;font-size:25px;font-weight:600;line-height:36px}
.trust-number{font-size:76px;font-weight:700;line-height:70px;margin-left:16px}
.trust-years{font-size:27px;font-weight:600;margin-left:6px;line-height:36px}

.endorsements{position:absolute;left:639px;top:757px;width:561px;height:90px;background:var(--paper);clip-path:polygon(32px 0,100% 0,100% 100%,0 100%);display:flex;align-items:center;gap:20px;padding-left:64px}
.badge.round{width:54px;height:54px;border-radius:50%;background:#7a1f1f}
.badge.stars{width:72px;height:44px;background:#d32323;border-radius:4px}
.badge.listing{width:70px;height:54px;background:#b89a5e}
.badge.accredited{width:120px;height:44px;background:#1d6f94;border-radius:4px}
.badge.rating{width:64px;height:64px;border-radius:50%;background:#2a8fd0}

.footer-strip{position:absolute;left:0;top:847px;width:1200px;height:12px;background:var(--strip)}
.footer-band{position:absolute;left:0;top:859px;width:1200px;height:18px;background:var(--night)}
</style>
</head>
<body>
<div class="ad">
  <div class="skyline" role="img" aria-label="Faint dark city skyline photograph behind the ad"></div>

  <header class="header">
    <div class="brand"><span class="brand-mark"></span><span class="brand-name">MARVOLIN LAW</span></div>
    <div class="tagline">SHAPING FAITH WITH RESULTS</div>
    <div class="attorney-tab">Gordon R. Marvolin, Esq.</div>
  </header>

  <section class="practices">
    <div class="practice-list">
      <div>Personal Injury<span class="sep">|</span>Unlicensed Contractors<span class="sep">|</span>Legal Malpractice</div>
      <div>Medical Malpractice<span class="sep">|</span>Civil Litigation</div>
    </div>
  </section>

  <section class="contact">
    <div class="contact-item">
      <svg width="24" height="26" viewBox="0 0 24 24" fill="none" stroke="#1b1b1b" stroke-width="2"><path d="M6 3l3 4-2 2c1 3 4 6 7 7l2-2 4 3-2 4C10 21 3 14 3 5z"/></svg>
      <span>(888) 555-0142</span>
    </div>
    <div class="contact-item">
      <svg width="22" height="22" viewBox="0 0 24 24" fill="none" stroke="#1b1b1b" stroke-width="2"><circle cx="12" cy="12" r="10"/><ellipse cx="12" cy="12" rx="4" ry="10"/><path d="M2 12h20M4 7h16M4 17h16"/></svg>
      <span>marvolinlegal.com</span>
    </div>
    <div class="contact-item">
      <svg width="30" height="27" viewBox="0 0 24 22" fill="#1b1b1b"><path d="M12 1L1 11h3v10h6v-6h4v6h6V11h3z"/></svg>
      <span class="address">2180 Alder Crest Ave. | Suite 405<br>Linwood Heights, CA | 90417</span>
    </div>
  </section>

  <div class="portrait" role="img" aria-label="Black and white photo of the head attorney in a suit and tie"></div>

  <section class="calendar">
    <div class="month"><h3>JANUARY</h3><div class="days"><span>S</span><span>M</span><span>T</span><span>W</span><span>T</span><span>F</span><span>S</span><span></span><span>1</span><span>2</span><span>3</span><span>4</span><span>5</span><span>6</span><span>7</span><span>8</span><span>9</span><span>10</span><span>11</span><span>12</span><span>13</span><span>14</span><span>15</span><span>16</span><span>17</span><span>18</span><span>19</span><span>20</span><span>21</span><span>22</span><span>23</span><span>24</span><span>25</span><span>26</span><span>27</span><span>28</span><span>29</span><span>30</span><span>31</span></div></div>
    <div class="month"><h3>FEBRUARY</h3><div class="days"><span>S</span><span>M</span><span>T</span><span>W</span><span>T</span><span>F</span><span>S</span><span></span><span></span><span></span><span></span><span>1</span><span>2</span><span>3</span><span>4</span><span>5</span><span>6</span><span>7</span><span>8</span><span>9</span><span>10</span><span>11</span><span>12</span><span>13</span><span>14</span><span>15</span><span>16</span><span>17</span><span>18</span><span>19</span><span>20</span><span>21</span><span>22</span><span>23</span><span>24</span><span>25</span><span>26</span><span>27</span><span>28</span></div></div>
    <div class="month"><h3>MARCH</h3><div class="days"><span>S</span><span>M</span><span>T</span><span>W</span><span>T</span><span>F</span><span>S</span><span></span><span></span><span></span><span></span><span>1</span><span>2</span><span>3</span><span>4</span><span>5</span><span>6</span><span>7</span><span>8</span><span>9</span><span>10</span><span>11</span><span>12</span><span>13</span><span>14</span><span>15</span><span>16</span><span>17</span><span>18</span><span>19</span><span>20</span><span>21</span><span>22</span><span>23</span><span>24</span><span>25</span><span>26</span><span>27</span><span>28</span><span>29</span><span>30</span><span>31</span></div></div>
    <div class="month"><h3>APRIL</h3><div class="days"><span>S</span><span>M</span><span>T</span><span>W</span><span>T</span><span>F</span><span>S</span><span>1</span><span>2</span><span>3</span><span>4</span><span>5</span><span>6</span><span>7</span><span>8</span><span>9</span><span>10</span><span>11</span><span>12</span><span>13</span><span>14</span><span>15</span><span>16</span><span>17</span><span>18</span><span>19</span><span>20</span><span>21</span><span>22</span><span>23</span><span>24</span><span>25</span><span>26</span><span>27</span><span>28</span><span>29</span><span>30</span></div></div>
    <div class="month"><h3>MAY</h3><div class="days"><span>S</span><span>M</span><span>T</span><span>W</span><span>T</span><span>F</span><span>S</span><span></span><span></span><span>1</span><span>2</span><span>3</span><span>4</span><span>5</span><span>6</span><span>7</span><span>8</span><span>9</span><span>10</span><span>11</span><span>12</span><span>13</span><span>14</span><span>15</span><span>16</span><span>17</span><span>18</span><span>19</span><span>20</span><span>21</span><span>22</span><span>23</span><span>24</span><span>25</span><span>26</span><span>27</span><span>28</span><span>29</span><span>30</span><span>31</span></div></div>
    <div class="month"><h3>JUNE</h3><div class="days"><span>S</span><span>M</span><span>T</span><span>W</span><span>T</span><span>F</span><span>S</span><span></span><span></span><span></span><span></span><span></span><span>1</span><span>2</span><span>3</span><span>4</span><span>5</span><span>6</span><span>7</span><span>8</span><span>9</span><span>10</span><span>11</span><span>12</span><span>13</span><span>14</span><span>15</span><span>16</span><span>17</span><span>18</span><span>19</span><span>20</span><span>21</span><span>22</span><span>23</span><span>24</span><span>25</span><span>26</span><span>27</span><span>28</span><span>29</span><span>30</span></div></div>
    <div class="month"><h3>JULY</h3><div class="days"><span>S</span><span>M</span><span>T</span><span>W</span><span>T</span><span>F</span><span>S</span><span>1</span><span>2</span><span>3</span><span>4</span><span>5</span><span>6</span><span>7</span><span>8</span><span>9</span><span>10</span><span>11</span><span>12</span><span>13</span><span>14</span><span>15</span><span>16</span><span>17</span><span>18</span><span>19</span><span>20</span><span>21</span><span>22</span><span>23</span><span>24</span><span>25</span><span>26</span><span>27</span><span>28</span><span>29</span><span>30</span><span>31</span></div></div>
    <div class="month"><h3>AUGUST</h3><div class="days"><span>S</span><span>M</span><span>T</span><span>W</span><span>T</span><span>F</span><span>S</span><span></span><span></span><span></span><span>1</span><span>2</span><span>3</span><span>4</span><span>5</span><span>6</span><span>7</span><span>8</span><span>9</span><span>10</span><span>11</span><span>12</span><span>13</span><span>14</span><span>15</span><span>16</span><span>17</span><span>18</span><span>19</span><span>20</span><span>21</span><span>22</span><span>23</span><span>24</span><span>25</span><span>26</span><span>27</span><span>28</span><span>29</span><span>30</span><span>31</span></div></div>
    <div class="month"><h3>SEPTEMBER</h3><div class="days"><span>S</span><span>M</span><span>T</span><span>W</span><span>T</span><span>F</span><span>S</span><span></span><span></span><span></span><span></span><span></span><span></span><span>1</span><span>2</span><span>3</span><span>4</span><span>5</span><span>6</span><span>7</span><span>8</span><span>9</span><span>10</span><span>11</span><span>12</span><span>13</span><span>14</span><span>15</span><span>16</span><span>17</span><span>18</span><span>19</span><span>20</span><span>21</span><span>22</span><span>23</span><span>24</span><span>25</span><span>26</span><span>27</span><span>28</span><span>29</span><span>30</span></div></div>
    <div class="month"><h3>OCTOBER</h3><div class="days"><span>S</span><span>M</span><span>T</span><span>W</span><span>T</span><span>F</span><span>S</span><span></span><span>1</span><span>2</span><span>3</span><span>4</span><span>5</span><span>6</span><span>7</span><span>8</span><span>9</span><span>10</span><span>11</span><span>12</span><span>13</span><span>14</span><span>15</span><span>16</span><span>17</span><span>18</span><span>19</span><span>20</span><span>21</span><span>22</span><span>23</span><span>24</span><span>25</span><span>26</span><span>27</span><span>28</span><span>29</span><span>30</span><span>31</span></div></div>
    <div class="month"><h3>NOVEMBER</h3><div class="days"><span>S</span><span>M</span><span>T</span><span>W</span><span>T</span><span>F</span><span>S</span><span></span><span></span><span></span><span></span><span>1</span><span>2</span><span>3</span><span>4</span><span>5</span><span>6</span><span>7</span><span>8</span><span>9</span><span>10</span><span>11</span><span>12</span><span>13</span><span>14</span><span>15</span><span>16</span><span>17</span><span>18</span><span>19</span><span>20</span><span>21</span><span>22</span><span>23</span><span>24</span><span>25</span><span>26</span><span>27</span><span>28</span><span>29</span><span>30</span></div></div>
    <div class="month"><h3>DECEMBER</h3><div class="days"><span>S</span><span>M</span><span>T</span><span>W</span><span>T</span><span>F</span><span>S</span><span></span><span></span><span></span><span></span><span></span><span></span><span>1</span><span>2</span><span>3</span><span>4</span><span>5</span><span>6</span><span>7</span><span>8</span><span>9</span><span>10</span><span>11</span><span>12</span><span>13</span><span>14</span><span>15</span><span>16</span><span>17</span><span>18</span><span>19</span><span>20</span><span>21</span><span>22</span><span>23</span><span>24</span><span>25</span><span>26</span><span>27</span><span>28</span><span>29</span><span>30</span><span>31</span></div></div>
  </section>

  <div class="year-tab"></div>
  <div class="year">2018</div>

  <section class="trust">
    <div class="trust-lines">Known and Trusted in<br>Our Community for over</div>
    <div class="trust-number">22</div>
    <div class="trust-years">Years</div>
  </section>

  <section class="endorsements" aria-label="Endorsements">
    <span class="badge round"></span>
    <span class="badge stars"></span>
    <span class="badge listing"></span>
    <span class="badge accredited"></span>
    <span class="badge rating"></span>
  </section>

  <div class="footer-strip"></div>
  <div class="footer-band"></div>
</div>
</body>
</html>
```